Full page ad in a magazine

We would like an ad designed to be placed for advertising in magazines, theater playbills, etc. I have attached a copy of some previous ads that were done for us, although they need much improvement and redesigned. We have won "best chiropractor" awards that can be seen on our website home page at ferncliffspineandjoint.com

```html
<!DOCTYPE html>
<html lang="en">
<head>
<meta charset="utf-8">
<title>Ferncliff Spine &amp; Joint Center – Magazine Ad</title>
<link href="https://fonts.googleapis.com/css2?family=Poppins:wght@400;500;600;700;800&display=swap" rel="stylesheet">
<style>
  :root {
    --red: #8b0a0a;
    --grey-head: #a6a6a8;
    --ink: #1f1f1f;
    --black: #1c1c1c;
    --icon-grey: #9a9a9c;
    --paper: #ffffff;
    --stage: #eeeef0;
    --badge-blue: #2a3fd6;
    --badge-gold: #e8bf2a;
  }
  * { margin: 0; padding: 0; box-sizing: border-box; }
  html, body { width: 1200px; height: 2400px; overflow: hidden; }
  body { background: var(--stage); font-family: "Poppins", sans-serif; color: var(--ink); position: relative; }

  .ad {
    position: absolute; left: 0; top: 424px;
    width: 1034px; height: 1338px;
    background: var(--paper);
    transform: scale(1.1605); transform-origin: top left;
    overflow: hidden;
  }
  .abs { position: absolute; }

  .headline { left: 48px; top: 38px; font-weight: 800; font-size: 126px; line-height: 100px; letter-spacing: -2px; }
  .headline .line-red { color: var(--red); display: block; }
  .headline .line-grey { color: var(--grey-head); display: block; }

  .service-band { left: 47px; top: 272px; height: 76px; display: flex; }
  .service-band span { display: flex; align-items: center; font-weight: 800; font-size: 46px; color: #fff; }
  .band-red { background: var(--red); width: 427px; padding-left: 30px; }
  .band-black { background: var(--black); width: 307px; padding-left: 24px; }

  .treating-title { left: 58px; top: 375px; font-weight: 700; font-size: 40px; }
  .guide { left: 0; top: 0; }

  .conditions { left: 93px; top: 462px; display: grid; grid-template-columns: 305px 300px; row-gap: 20px; }
  .condition { display: flex; align-items: center; gap: 12px; height: 52px; font-size: 27px; }
  .condition .dot { width: 52px; height: 52px; border-radius: 50%; flex: none; position: relative; }
  .dot.red { background: var(--red); }
  .dot.grey { background: var(--icon-grey); }
  .dot::after { content: ""; position: absolute; left: 18px; top: 18px; width: 16px; height: 16px; border-radius: 50%; background: #fff; opacity: .85; }
  .divider { left: 350px; top: 456px; width: 2px; height: 205px; background: #d6d6d6; }
  .insurance { left: 92px; top: 672px; font-size: 26px; }

  .doctor-photo { left: 53px; top: 737px; width: 134px; height: 134px; border-radius: 50%; border: 5px solid #d9d9d9; background: radial-gradient(circle at 50% 40%, #c9a58c 0%, #7a6a62 55%, #3a3a3a 100%); z-index: 2; }
  .name-bar { left: 170px; top: 762px; width: 404px; height: 80px; background: var(--red); border-radius: 0 8px 8px 0; color: #fff; font-weight: 700; font-size: 39px; display: flex; align-items: center; padding-left: 40px; }
  .hours { left: 210px; top: 843px; font-size: 21px; font-weight: 500; }

  .contact { left: 72px; top: 890px; }
  .contact-row { display: flex; gap: 14px; align-items: flex-start; margin-bottom: 6px; }
  .contact-row svg { flex: none; margin-top: 4px; }
  .phone { font-weight: 700; font-size: 29px; line-height: 42px; }
  .address { font-size: 22px; line-height: 28px; }
  .vote { font-weight: 700; font-size: 22px; line-height: 34px; }

  .brand { left: 65px; top: 1088px; display: flex; align-items: center; gap: 14px; }
  .brand-square { width: 96px; height: 104px; background: #d4d4d6; }
  .brand-name { font-weight: 700; font-size: 34px; line-height: 40px; color: var(--red); }

  .badge-best { left: 808px; top: 63px; width: 172px; height: 147px; background: var(--badge-blue); }
  .badge-star { left: 835px; top: 270px; width: 120px; height: 120px; border-radius: 50%; background: #111; box-shadow: 0 0 0 8px var(--badge-gold); }
  .badge-choice { left: 782px; top: 458px; width: 200px; height: 78px; border-radius: 40px; border: 3px solid #bdbdbd; }

  .hiker-photo { left: 600px; top: 590px; width: 434px; height: 670px; border-radius: 220px 0 0 0; background: linear-gradient(170deg, #9c9c9e 0%, #6b6b6d 40%, #8b1414 60%, #3e3e40 85%, #2a2a2a 100%); }

  .footer { left: 0; top: 1250px; width: 1034px; height: 88px; background: var(--black); color: #fff; display: flex; align-items: center; justify-content: center; font-size: 28px; letter-spacing: 4px; }
  .footer b { font-weight: 700; }
</style>
</head>
<body>
<main class="ad">
  <h1 class="abs headline"><span class="line-red">NECK OR</span><span class="line-grey">BACK PAIN?</span></h1>

  <div class="abs service-band"><span class="band-red">CHIROPRACTIC</span><span class="band-black">MESSAGE</span></div>

  <div class="abs badge-best" role="img" aria-label="Award badge"></div>
  <div class="abs badge-star" role="img" aria-label="Readers' choice award badge"></div>
  <div class="abs badge-choice" role="img" aria-label="Choice awards badge"></div>

  <div class="abs hiker-photo" role="img" aria-label="Photo of a hiker with a red backpack resting on a rock"></div>

  <h2 class="abs treating-title">Treating</h2>
  <svg class="abs guide" width="1034" height="760" viewBox="0 0 1034 760">
    <g fill="none" stroke="#8b0a0a" stroke-width="1.5" stroke-dasharray="6 4">
      <path d="M255 402 H753 Q763 402 763 412 V600"/>
      <path d="M60 445 V718 Q60 728 70 728 H735"/>
    </g>
    <circle cx="255" cy="402" r="5" fill="#8b0a0a"/>
    <circle cx="60" cy="445" r="5" fill="#8b0a0a"/>
  </svg>

  <ul class="abs conditions" style="list-style:none">
    <li class="condition"><span class="dot red"></span>Back Pain</li>
    <li class="condition"><span class="dot grey"></span>Joint Pain</li>
    <li class="condition"><span class="dot grey"></span>Neck Pain</li>
    <li class="condition"><span class="dot red"></span>Sciatica</li>
    <li class="condition"><span class="dot red"></span>Headaches</li>
    <li class="condition"><span class="dot grey"></span>Fatigue</li>
  </ul>
  <div class="abs divider"></div>
  <p class="abs insurance">Medicare and most Insurance accepted.</p>

  <div class="abs doctor-photo" role="img" aria-label="Portrait photo of the chiropractor"></div>
  <div class="abs name-bar">Marcus Hale, DC</div>
  <p class="abs hours">OPEN MONDAY - SATURDAY</p>

  <div class="abs contact">
    <div class="contact-row">
      <svg width="28" height="28" viewBox="0 0 24 24"><path fill="#9a9a9c" d="M6.6 10.8a15 15 0 0 0 6.6 6.6l2.2-2.2a1 1 0 0 1 1-.25 11.4 11.4 0 0 0 3.6.57 1 1 0 0 1 1 1V20a1 1 0 0 1-1 1A17 17 0 0 1 3 4a1 1 0 0 1 1-1h3.5a1 1 0 0 1 1 1c0 1.25.2 2.45.57 3.57a1 1 0 0 1-.25 1z"/></svg>
      <span class="phone">555.210.4478</span>
    </div>
    <div class="contact-row">
      <svg width="28" height="30" viewBox="0 0 24 24"><path fill="#9a9a9c" d="M12 2a7 7 0 0 0-7 7c0 5.2 7 13 7 13s7-7.8 7-13a7 7 0 0 0-7-7zm0 9.5A2.5 2.5 0 1 1 12 6.5a2.5 2.5 0 0 1 0 5z"/></svg>
      <p class="address">EAST RIDGE LOCATION<br>2150 Alder Row, Suite 3<br>Ferncliff, VA 20199</p>
    </div>
    <div class="contact-row">
      <svg width="28" height="28" viewBox="0 0 24 24"><path fill="#9a9a9c" d="M4 20h16v2H4zM14.6 3.4l3 3L9 15l-3.6.6L6 12z"/></svg>
      <span class="vote">Vote for us: www.regionreaders.com/vote</span>
    </div>
  </div>

  <div class="abs brand">
    <span class="brand-square"></span>
    <span class="brand-name">Ferncliff<br>Spine &amp; Joint Center</span>
  </div>

  <footer class="abs footer"><span>www.<b>ferncliffspineandjoint</b>.com</span></footer>
</main>
</body>
</html>
```